Solar Energy Company Overview Presentation

Hello designers,

Our company Kelvara Energy Solutions is looking to re-design our company overview presentation labeled "Statement of Qualifications". Currently this document is provided in .doc and .PDF formats to clients and partners.

We would like to keep a professional and clean look, while making it look more sleek and up to do date with more modern design standards. Please see attached document for the current layout.

In addition we would like to add a page for corporate leadership, that is not currently on the document. It will have a photo of team member, title, and bio.

This should be a template that can be edited in the future with Microsoft word if possible. We also have the capabilities to use Photoshop if needed.

I have attached our current document titled "Statement of Qualifications" so you can view the type of content that is on it. I also attached other marketing items so you can get an idea of how some of our other branding looks. I have also attached the font we like to use. Please feel free to take you own creative direction.

Our website is http://kelvaraenergy.example

Thank you for your consideration, please message me with any questions.

Dorian

Target Market(s)

Solar Industry Companies and Clients

Industry/Entity Type

It Company

Requirements
Must have
• Professional Design With Modern High-End Look

```html
<!DOCTYPE html>
<html lang="en">
<head>
<meta charset="utf-8">
<title>Kelvara Energy Solutions – Statement of Qualifications</title>
<link href="https://fonts.googleapis.com/css2?family=Raleway:ital,wght@0,400;0,600;0,700;0,800;1,400;1,700&display=swap" rel="stylesheet">
<style>
  :root {
    --backdrop: #e6e6e6;
    --page: #ffffff;
    --page-edge: #cfcfcf;
    --orange: #f07a22;
    --ink: #1b1b1b;
    --heading-grey: #6e6e6e;
    --body-grey: #3a3a3a;
    --sky-top: #36b9e6;
    --sky-low: #a9dcef;
  }
  * { box-sizing: border-box; margin: 0; padding: 0; }
  html, body {
    width: 1200px; height: 776px; overflow: hidden;
    background: var(--backdrop);
    font-family: "Raleway", sans-serif;
  }
  .spread { position: relative; width: 1200px; height: 776px; }
  .page {
    position: absolute; top: 12px; width: 582px; height: 753px;
    background: var(--page); border: 1px solid var(--page-edge); overflow: hidden;
  }
  .page--cover { left: 12px; }
  .page--leadership { left: 606px; }

  /* Cover */
  .cover-photo {
    position: absolute; inset: 0;
    background: linear-gradient(180deg, var(--sky-top) 0%, #6cc9ec 26%, var(--sky-low) 40%, #9aa38f 48%, #6e7a5e 58%, #7f8478 64%, #3f5a8e 76%, #2b3f72 90%, #4a5670 100%);
  }
  .cover-brand {
    position: absolute; left: 0; right: 44px; top: 104px;
    text-align: right;
    font-weight: 800; font-size: 50px; line-height: 1.02; color: var(--ink);
    letter-spacing: -0.5px;
  }
  .cover-tagline {
    position: absolute; left: 0; right: 28px; top: 210px; text-align: right;
    font-style: italic; font-size: 14.5px; color: var(--orange);
  }

  /* Leadership page */
  .page-brand {
    position: absolute; top: 20px; right: 16px;
    font-size: 11px; font-weight: 600; color: var(--heading-grey);
  }
  .page-title {
    position: absolute; top: 50px; left: 0; right: 0; text-align: center;
    font-size: 21px; font-weight: 700; color: var(--heading-grey); letter-spacing: 0.3px;
  }
  .page-title__bracket { color: var(--orange); font-size: 30px; font-weight: 600; vertical-align: -2px; }
  .section { position: absolute; left: 38px; right: 34px; }
  .section--intro { top: 122px; }
  .section--expertise { top: 396px; }
  .section__heading {
    font-size: 13px; font-weight: 800; color: var(--orange); margin-bottom: 9px;
  }
  .section p {
    font-size: 10.3px; line-height: 1.55; color: var(--body-grey);
    text-align: justify; margin-bottom: 9px;
  }
  .highlight { color: var(--orange); font-weight: 700; font-style: italic; }
  .field-photo {
    position: absolute; left: 0; right: 0; top: 546px; bottom: 0;
    background: linear-gradient(175deg, #d9e7ee 0%, #c9dbe4 10%, #3f6fd6 22%, #2a58c8 55%, #1e45b0 75%, #8c7a5e 88%, #a38f6d 100%);
  }
</style>
</head>
<body>
<main class="spread">
  <section class="page page--cover">
    <div class="cover-photo" role="img" aria-label="Aerial view of a city rooftop covered with rows of solar panels under a blue sky, skyline in the distance"></div>
    <div class="cover-brand">Kelvara<br>Energy</div>
    <p class="cover-tagline">Clean, Safe, Renewable Energy of the future</p>
  </section>

  <section class="page page--leadership">
    <div class="page-brand">Kelvara Energy</div>
    <h1 class="page-title"><span class="page-title__bracket">[</span>CORPORATE LEADERSHIP<span class="page-title__bracket">]</span></h1>

    <div class="section section--intro">
      <h2 class="section__heading">INTRODUCTION</h2>
      <p>Kelvara Energy Solutions and the Kelvara Group, family of companies, provide renewable energy solutions and services. We specialize in developing, financing, constructing, owning and operating solar and wind energy generation facilities. Facilities which range from small distributed generation to utility scale projects located across North America and the Pacific Islands. At Kelvara Energy Solutions, we believe in creating power from sustainable, clean resources that will benefit our communities.</p>
      <p>With the global push towards cleaner and more efficient ways of producing electricity, Kelvara Energy Solutions has come to the forefront of the industry to lead the charge. Our company's experience, innovative approach, business partners, and sponsorship have caused a growth that can only be measured by leaps and bounds.</p>
      <p>With segregations in the market, the founding members of Kelvara Energy Solutions saw a need to create a conglomerate. By affectively bringing all of the parties involved in a renewable energy project under one umbrella, Kelvara Energy Solutions can take a project from its inception to operation in the most efficient approach possible.</p>
    </div>

    <div class="section section--expertise">
      <h2 class="section__heading">EXPERTISE</h2>
      <p>The founding members of Kelvara Energy Solutions have over 40 combined years in the industry. In that time, our record has been flawless in bringing projects to fruition. Our employees are specialty-trained for the benefit of our clients and those looking to benefit from clean energy. We are focused on <span class="highlight">value</span>, <span class="highlight">safety</span>, and <span class="highlight">sustainability</span>.</p>
    </div>

    <div class="field-photo" role="img" aria-label="Ground-mounted blue solar panel array on dry grass with trees in the background"></div>
  </section>
</main>
</body>
</html>
```